The Brambury Firm

We need a new design for our letterhead and envelopes. We are a personal injury and criminal defense firm so we need something modern and clean, but more on the professional/traditional side. Our new logo has two colors and is attached to the file so we need something that works well with those colors/matches the design. The following information needs to be on the letterhead:
Phone: (555) 314-7265
Fax: (555) 419-6032
Toll-Free: (555) 736-1149
Post Office Box 4273
Lexington, SC 29458-4273
TQHarmClaimsDesk.example
PalmettoShieldCounsel.example

Target Market(s)

Clients, government agencies, other law firms

Industry/Entity Type

Legal

Font styles to use
Sans Serif
Other font styles liked:
• Arial

Colors

Designer to choose colors to be used in the design.

Requirements
Must have
• Must look professional and clean, modern
Nice to have
• I would like to see a design that works with the logo but does not distract from the content that will be printed on it
Should not have
• Too many colors or crazy designs.

```html
<!DOCTYPE html>
<html lang="en">
<head>
<meta charset="utf-8">
<title>The Brambury Firm — Stationery</title>
<link href="https://fonts.googleapis.com/css2?family=Source+Sans+3:wght@400;600&display=swap" rel="stylesheet">
<style>
  :root {
    --backdrop: #7a7a7a;
    --paper: #f5f4f2;
    --brand-red: #d21c22;
    --brand-navy: #2a2f8f;
    --ink: #3a3a3a;
    --ink-soft: #4a4a4a;
    --sig-tone: #2b2b2b;
  }
  * { margin: 0; padding: 0; box-sizing: border-box; }
  html, body { width: 1200px; height: 793px; overflow: hidden; }
  body {
    background: var(--backdrop);
    font-family: "Source Sans 3", Arial, sans-serif;
    color: var(--ink);
    position: relative;
  }
  .sheet {
    position: absolute;
    background: var(--paper);
    box-shadow: 0 2px 6px rgba(0,0,0,.35);
  }
  .letterhead { left: 82px; top: 62px; width: 475px; height: 668px; }
  .brand-name {
    font-weight: 600;
    color: var(--brand-navy);
    text-transform: uppercase;
    letter-spacing: .06em;
    white-space: nowrap;
  }
  .letterhead .brand-name {
    position: absolute; top: 78px; left: 0; width: 100%;
    text-align: center; font-size: 20px;
  }
  .salutation {
    position: absolute; left: 48px; top: 187px; font-size: 13px; color: var(--ink-soft);
  }
  .letter-body {
    position: absolute; left: 48px; top: 226px; width: 381px;
    font-size: 7.2px; line-height: 11.4px; text-align: justify;
  }
  .letter-body p { margin-bottom: 11.4px; }
  .closing { position: absolute; left: 48px; top: 466px; font-size: 7.2px; }
  .signature {
    position: absolute; left: 48px; top: 482px; width: 62px; height: 22px;
    background: linear-gradient(90deg, rgba(43,43,43,.15), rgba(43,43,43,.35), rgba(43,43,43,.1));
    border-radius: 10px;
  }
  .signer { position: absolute; left: 48px; top: 520px; font-size: 8px; line-height: 10px; }
  .letter-footer {
    position: absolute; left: 0; top: 604px; width: 100%;
    text-align: center; font-size: 7.6px; line-height: 9.6px; color: var(--ink-soft);
  }
  .letter-footer b { font-weight: 600; }

  .envelope-back { left: 578px; top: 224px; width: 531px; height: 242px; }
  .envelope-back svg { position: absolute; left: 0; top: 0; }
  .envelope-back .brand-name {
    position: absolute; top: 42px; left: 0; width: 100%;
    text-align: center; font-size: 13px; color: #fff;
  }
  .envelope-front { left: 578px; top: 487px; width: 532px; height: 242px; }
  .envelope-front .brand-name { position: absolute; left: 28px; top: 56px; font-size: 19px; }
  .return-address {
    position: absolute; left: 36px; top: 103px; font-size: 8px; line-height: 10px; color: var(--ink-soft);
  }
</style>
</head>
<body>

<section class="sheet letterhead">
  <div class="brand-name">The Brambury Firm</div>
  <p class="salutation">Dear Mr. Calloway,</p>
  <div class="letter-body">
    <p>Lorem ipsum dolor sit amet, consectetur adipiscing elit. Donec orci purus, luctus vitae dignissim eu, iaculis sed purus. Vivamus faucibus, ipsum nec aliquet viverra, leo mauris condimentum ligula, sit amet sagittis enim ligula quis arcu. Nam egestas tortor id nisi porttitor mattis. In tortor ante, ultricies in suscipit a, tempus non massa. Vivamus et auctor mi. Fusce vel massa nulla. Phasellus nec eros mauris, et scelerisque orci.</p>
    <p>Donec malesuada orci vitae nulla accumsan porta a id massa. Quisque accumsan iaculis magna sit amet fringilla. Maecenas consequat, magna eget tincidunt semper, odio nibh rutrum mi, id feugiat ante nisi eu risus. Vestibulum nunc orci, rhoncus a placerat in, ultricies in mi. Cras mattis varius eros, vel fringilla nisi suscipit eget. Quisque scelerisque sagittis nulla at porttitor.</p>
    <p>Sed id augue vitae urna euismod commodo aliquet a quam. Pellentesque arcu velit, cursus et malesuada ut, consequat et diam. Nullam erat sem, rhoncus id ullamcorper vitae, rhoncus et arcu. In ultricies ultricies nulla, ut rutrum nisi iaculis at. Donec eu magna a metus ornare faucibus. Fusce aliquet faucibus ultricies. Morbi semper, est id tincidunt gravida, sem arcu adipiscing lacus, ac bibendum nulla leo eu purus. Quisque nec diam sed risus consectetur a cursus quis quis nibh. Vestibulum id purus lorem.</p>
    <p>It is a long established fact that a reader will be distracted by the readable content of a page when looking at its layout. The point of using Lorem Ipsum is that it has a more-or-less normal distribution of letters, as opposed to using 'Content here, content here', making it look like readable English. Many desktop publishing packages</p>
  </div>
  <p class="closing">Sincerely,</p>
  <div class="signature" role="img" aria-label="Handwritten signature"></div>
  <p class="signer">Daniel Hartwell<br>CEO/ Founder</p>
  <div class="letter-footer">
    <b>TF:</b> (555) 736-1149 <b>P:</b> (555) 314-7265 <b>F:</b> (555) 419-6032<br>
    www.TQHarmClaimsDesk.example | www.PalmettoShieldCounsel.example<br>
    Post Office Box 4273, Lexington, SC 29458-4273
  </div>
</section>

<section class="sheet envelope-back">
  <svg width="531" height="242" viewBox="0 0 531 242" aria-hidden="true">
    <path d="M0 0 H531 L517 68 Q510 88 490 88 H41 Q21 88 14 68 Z" fill="var(--brand-red)"/>
  </svg>
  <div class="brand-name">The Brambury Firm</div>
</section>

<section class="sheet envelope-front">
  <div class="brand-name">The Brambury Firm</div>
  <p class="return-address">Post Office Box 4273<br>Lexington, SC 29458-4273</p>
</section>

</body>
</html>
```